Corvale Homes

To produce a business card design for our newly established house building and development company, We have had a logo design done please see attached, our slogan is "building your home sweet home"
Contact Information for Business Card
Adress on card needs to Read - 58 Elmsworth Lane, Kettering, Northamptonshire NN16 4QT. Director name Dean Vascotti
Requirements
Must have
- Web adress is www.corvale-homes.co.uk
- Email address is info@corvale-homes.co.uk
- phone number 07700 900417

```html
<!DOCTYPE html>
<html lang="en">
<head>
<meta charset="utf-8">
<title>Corvale Homes – Business Card</title>
<link rel="stylesheet" href="https://fonts.googleapis.com/css2?family=Lato:wght@400;700&display=swap">
<style>
  :root {
    --stage: #000000;
    --card-white: #ffffff;
    --brand-green: #8cc63f;
    --pattern-green: #a3d266;
    --ink: #3a3a3a;
    --rule: #b5b5b5;
  }
  * { margin: 0; padding: 0; box-sizing: border-box; }
  html, body {
    width: 1200px; height: 900px; overflow: hidden;
    background: var(--stage);
    font-family: "Lato", sans-serif;
  }
  .canvas { position: relative; width: 1200px; height: 900px; }
  .card {
    position: absolute; top: 306px;
    width: 440px; height: 271px;
    border-radius: 10px; overflow: hidden;
  }
  .card-front { left: 149px; background: var(--card-white); }
  .card-back { left: 608px; background: var(--brand-green); }

  .brand-block {
    position: absolute; left: 22px; top: 0; width: 190px; height: 271px;
    display: flex; align-items: center; justify-content: center;
  }
  .brand-name {
    display: flex; align-items: center; gap: 8px;
    color: var(--brand-green);
    font-weight: 700; font-size: 20px; letter-spacing: 0.5px;
    text-transform: uppercase; white-space: nowrap;
  }
  .brand-dot { width: 12px; height: 12px; background: var(--brand-green); }

  .divider {
    position: absolute; left: 227px; top: 74px;
    width: 1px; height: 122px; background: var(--rule);
  }
  .contact-block {
    position: absolute; left: 246px; top: 71px;
    color: var(--ink); font-size: 12.5px; line-height: 15px;
  }
  .person-name {
    color: var(--brand-green); font-weight: 700; font-size: 14.5px;
    text-transform: uppercase; line-height: 17px;
  }
  .person-role { margin-bottom: 12px; }
  .contact-line { display: flex; align-items: center; gap: 4px; }
  .contact-line svg { width: 10px; height: 10px; flex: none; }
  .address { margin-top: 9px; }

  .back-pattern {
    position: absolute; inset: 0;
    background: linear-gradient(135deg, var(--brand-green), #94ca4c 50%, var(--brand-green));
  }
  .back-brand {
    position: absolute; left: 260px; top: 118px;
    color: var(--card-white); font-weight: 700; font-size: 17px;
    text-transform: uppercase; white-space: nowrap;
  }
</style>
</head>
<body>
<main class="canvas">
  <section class="card card-front">
    <div class="brand-block">
      <div class="brand-name"><span class="brand-dot"></span>Corvale Homes</div>
    </div>
    <div class="divider"></div>
    <div class="contact-block">
      <p class="person-name">Dean Vascotti</p>
      <p class="person-role">Director</p>
      <p class="contact-line">
        <svg viewBox="0 0 10 10" aria-hidden="true"><path d="M1 4 Q5 0 9 4 L8 5 L6.5 4 L6.5 3.5 Q5 3 3.5 3.5 L3.5 4 L2 5 Z M2.5 6 H7.5 V9 H2.5 Z" fill="var(--brand-green)"/></svg>
        07700 900417
      </p>
      <p class="contact-line">
        <svg viewBox="0 0 10 10" aria-hidden="true"><rect x="0.5" y="2" width="9" height="6.5" fill="var(--brand-green)"/><path d="M0.5 2 L5 6 L9.5 2" stroke="#fff" stroke-width="0.8" fill="none"/></svg>
        info@corvale-homes.co.uk
      </p>
      <p class="contact-line">
        <svg viewBox="0 0 10 10" aria-hidden="true"><circle cx="5" cy="5" r="4.5" fill="var(--brand-green)"/><path d="M3 3 Q5 4 4 6 Q6 7 7 5" stroke="#fff" stroke-width="0.9" fill="none"/></svg>
        www.corvale-homes.co.uk
      </p>
      <p class="address">58 Elmsworth Lane, Kettering,<br>Northamptonshire NN16 4QT</p>
    </div>
  </section>

  <section class="card card-back">
    <div class="back-pattern" role="img" aria-label="Faint repeating brand pattern on green"></div>
    <div class="back-brand">Corvale Homes</div>
  </section>
</main>
</body>
</html>
```